looking to have a web site for the company which provides services in the industrial and commercial sectors such as: electrical, automation control and system integration, construction and maintenance, millwright, equipment assembly repair and installation. I have the domain already brivanholdings.net and logo. Most recent projects fulfilled for the following clients: MarlowKibbleCo, Dunholt University, OKSU, FALSTO, Tazzik, Prairie Grains

Target Market(s)

industrial and commercial sectors in electrical, automation, millwright and fabrication fields

Industry/Entity Type

Industrial

Coding

Coded - Design and coding required

Number of Pages Required

5+ page

Font styles to use
Sans Serif

Colors

Designer to choose colors to be used in the design.

Requirements
Nice to have
• looking to get something not complicated, nicely presented with minimum or no scrolling

```html
<!DOCTYPE html>
<html lang="en">
<head>
<meta charset="utf-8">
<title>Brivanholdings – Industrial &amp; Commercial Services</title>
<link href="https://fonts.googleapis.com/css2?family=Exo+2:wght@400;500;600;700&family=Open+Sans:ital,wght@0,400;0,600;1,400&display=swap" rel="stylesheet">
<style>
:root{
  --blue:#1a9fe0;
  --blue-dark:#0d78b8;
  --blue-deep:#0b5f95;
  --ink:#333a40;
  --grey:#666e75;
  --grey-light:#e9eaeb;
  --white:#ffffff;
  --head:"Exo 2", sans-serif;
  --body:"Open Sans", sans-serif;
}
*{margin:0;padding:0;box-sizing:border-box}
html,body{width:1200px;height:2990px;overflow:hidden}
body{position:relative;background:var(--white);font-family:var(--body);color:var(--ink)}
.abs{position:absolute}
svg{display:block}

/* header */
.site-header{left:0;top:0;width:1200px;height:116px;background:linear-gradient(#f6f6f6,#d9dadb)}
.brand{left:78px;top:24px;font-family:var(--head);font-weight:700;color:var(--blue);line-height:1}
.brand-name{font-size:46px;letter-spacing:1px}
.brand-sub{font-size:17px;letter-spacing:11px;margin-top:4px}
.call-top{left:878px;top:26px;display:flex;gap:14px;align-items:center}
.call-top small{display:block;font-size:14px;color:var(--ink)}
.call-top strong{display:block;font-family:var(--head);font-size:30px;font-weight:600;color:var(--blue);line-height:1.1}

/* hero */
.hero{left:0;top:116px;width:1200px;height:564px}
.hero-photo{width:100%;height:100%;background:linear-gradient(120deg,#4a5259,#6b7378 45%,#3d4449)}
.main-nav{left:78px;top:116px;width:1046px;height:60px}
.nav-shape{position:absolute;inset:0}
.nav-list{position:absolute;left:40px;top:0;height:60px;display:flex;list-style:none;align-items:center}
.nav-list li{font-family:var(--head);font-size:15px;color:var(--white);padding:0 0;text-transform:uppercase;height:60px;display:flex;align-items:center;justify-content:center;border-right:1px solid rgba(255,255,255,.25)}
.nav-list li.active{font-weight:700;gap:8px}
.nav-search{position:absolute;left:828px;top:0;width:178px;height:60px;display:flex;align-items:center;justify-content:space-between;color:var(--white);font-size:14px}
.hero-title{left:0;width:1200px;top:300px;text-align:center;font-family:var(--head);font-weight:600;font-size:46px;line-height:62px;color:var(--white);text-shadow:0 2px 6px rgba(0,0,0,.4)}
.hero-text{left:200px;width:800px;top:436px;text-align:center;font-style:italic;font-size:15px;line-height:26px;color:var(--white)}
.btn{display:flex;align-items:center;justify-content:center;font-family:var(--head);font-size:22px;color:var(--white);text-transform:uppercase}
.btn-solid{background:var(--blue);border-radius:4px}
.btn-outline{border:2px solid var(--white);border-radius:6px}
.hero-btn{left:502px;top:506px;width:198px;height:56px}
.hero-arrow{top:380px}

/* welcome */
.welcome{left:0;top:680px;width:1200px;height:458px;background:var(--blue)}
.welcome-kicker{left:78px;top:730px;font-family:var(--head);font-size:20px;color:var(--white)}
.welcome-title{left:78px;top:756px;font-family:var(--head);font-weight:600;font-size:42px;color:var(--white)}
.welcome-text{left:80px;top:822px;width:600px;font-style:italic;font-size:13px;line-height:27px;color:var(--white)}
.welcome-text p+p{margin-top:8px}
.welcome-btn{left:78px;top:1014px;width:198px;height:56px}
.frame{border:2px solid var(--white)}
.welcome-frame{left:760px;top:738px;width:364px;height:310px}
.welcome-photo{left:740px;top:756px;width:364px;height:316px;background:linear-gradient(#c5ccd2,#8b9297 60%,#6a6258)}

/* services */
.services{left:0;top:1138px;width:1200px;height:670px;background:linear-gradient(#ffffff 70%,#e6e7e8)}
.section-title{left:0;width:1200px;text-align:center;font-family:var(--head);font-size:40px;color:#555b60;font-weight:400}
.section-title b{color:var(--blue);font-weight:700}
.tabs{left:78px;top:1274px;width:1046px;height:78px;display:flex;border-radius:6px;overflow:hidden;background:linear-gradient(#f4f4f4,#d6d7d8);list-style:none}
.tabs li{display:flex;align-items:center;justify-content:center;text-align:center;font-size:15px;line-height:22px;color:#3c4247;text-transform:uppercase}
.tabs li.active{background:var(--blue);color:var(--white)}
.service-frame{left:78px;top:1412px;width:362px;height:308px;border-color:var(--blue)}
.service-photo{left:98px;top:1432px;width:362px;height:312px;background:linear-gradient(135deg,#d8dcdf,#7d8a95 50%,#2c3a4e)}
.service-title{left:496px;top:1428px;font-family:var(--head);font-weight:600;font-size:30px;color:var(--blue)}
.service-text{left:498px;top:1484px;width:590px;font-size:13px;line-height:27px;color:var(--grey)}
.service-text p+p{margin-top:8px}
.service-btn{left:496px;top:1668px;width:198px;height:56px}

/* call band */
.call-band{left:0;top:1806px;width:1200px;height:290px;background:var(--blue)}
.band-title{left:0;width:1200px;top:1864px;text-align:center;font-family:var(--head);font-weight:600;font-size:34px;color:var(--white)}
.band-text{left:200px;width:800px;top:1918px;text-align:center;font-size:13px;line-height:27px;color:var(--white)}
.band-call{left:368px;top:1988px;display:flex;align-items:center;gap:18px;font-size:32px;color:var(--white)}
.band-call .icon-circle{width:72px;height:72px;border-radius:50%;background:var(--blue-deep);display:flex;align-items:center;justify-content:center}

/* news */
.news-card{top:2236px;width:322px}
.news-photo{width:322px;height:200px;background:linear-gradient(135deg,#9aa39c,#5c6662 60%,#2f3634)}
.news-date{position:absolute;left:0;top:162px;width:76px;height:96px;background:var(--blue);color:var(--white);text-align:center;font-family:var(--head)}
.news-date b{display:block;font-size:38px;line-height:52px;font-weight:600;margin-top:4px}
.news-date span{font-size:15px}
.news-title{position:absolute;left:100px;top:208px;width:222px;font-size:19px;line-height:27px;color:#222}
.news-text{position:absolute;left:0;top:270px;width:322px;font-size:13px;line-height:27px;color:var(--grey)}

/* clients */
.clients{left:78px;top:2646px;width:1046px;height:106px}
.client-list{position:absolute;left:40px;top:0;width:966px;height:106px;display:flex;align-items:center;justify-content:space-around;list-style:none}
.client-list li{display:flex;align-items:center;gap:8px;font-family:var(--head);font-weight:700;font-size:22px;color:var(--white)}
.client-list li i{width:18px;height:18px;border-radius:50%;background:var(--white)}

/* footer */
.site-footer{left:0;top:2752px;width:1200px;height:238px;background:linear-gradient(#f3f3f3,#d3d4d5)}
.footer-nav{left:78px;top:2772px;display:flex;align-items:center;list-style:none;font-size:14px;color:var(--ink)}
.footer-nav li{padding:0 16px;border-left:1px solid #888;line-height:14px}
.footer-nav li.active{border:0;background:var(--blue);color:var(--white);padding:0;width:84px;height:46px;line-height:46px;text-align:center;border-radius:3px;margin-right:16px}
.footer-nav li.active+li{border-left:1px solid #888}
.social{left:966px;top:2780px;display:flex;gap:10px}
.social span{width:46px;height:46px;border-radius:50%;border:2px solid #9a9fa3}
.social span.on{background:var(--blue);border-color:var(--blue)}
.footer-label{left:78px;top:2872px;font-family:var(--head);font-weight:600;font-size:17px;color:var(--blue)}
.contact-item{top:2908px;display:flex;align-items:center;gap:14px;font-size:14px;color:var(--ink)}
.contact-item .icon-circle{width:52px;height:52px;border-radius:50%;background:var(--blue);display:flex;align-items:center;justify-content:center}
.copyright{left:878px;top:2914px;font-size:14px;line-height:24px;color:var(--ink)}
</style>
</head>
<body>

<header class="abs site-header">
</header>
<div class="abs brand">
  <div class="brand-name">BRIVAN</div>
  <div class="brand-sub">HOLDINGS LTD</div>
</div>
<div class="abs call-top">
  <svg width="44" height="44" viewBox="0 0 24 24"><path fill="#1a9fe0" d="M6.6 10.8a15.1 15.1 0 0 0 6.6 6.6l2.2-2.2c.3-.3.7-.4 1-.2 1.1.4 2.3.6 3.6.6.6 0 1 .4 1 1V20c0 .6-.4 1-1 1A17 17 0 0 1 3 4c0-.6.4-1 1-1h3.5c.6 0 1 .4 1 1 0 1.3.2 2.5.6 3.6.1.3 0 .7-.2 1z"/></svg>
  <div><small>Call Us Today :</small><strong>123 456 7890</strong></div>
</div>

<section class="abs hero">
  <div class="hero-photo" role="img" aria-label="Photo of an industrial plant interior with steel stairs and machinery"></div>
</section>
<nav class="abs main-nav">
  <svg class="nav-shape" width="1046" height="60" viewBox="0 0 1046 60"><defs><linearGradient id="navg" x1="0" y1="0" x2="0" y2="1"><stop offset="0" stop-color="#1fa8e8"/><stop offset="1" stop-color="#0f86c8"/></linearGradient></defs><path d="M0 0H1046L1016 60H30Z" fill="url(#navg)"/></svg>
  <ul class="nav-list">
    <li class="active" style="width:120px">Home <svg width="12" height="8" viewBox="0 0 12 8"><path d="M0 0H12L6 8Z" fill="#fff"/></svg></li>
    <li style="width:120px">About</li>
    <li style="width:126px">Services</li>
    <li style="width:126px">Clients</li>
    <li style="width:132px">News</li>
    <li style="width:140px">Contact</li>
  </ul>
  <div class="nav-search"><span>Search...</span>
    <svg width="22" height="22" viewBox="0 0 24 24"><circle cx="10" cy="10" r="7" fill="none" stroke="#fff" stroke-width="3"/><path d="M15 15l6 6" stroke="#fff" stroke-width="3" stroke-linecap="round"/></svg></div>
</nav>
<h1 class="abs hero-title">BRIVANHOLDINGS INDUSTRIAL&amp;<br>COMMERCIAL SERVICES</h1>
<p class="abs hero-text">Lorem Ipsum is simply dummy text of the printing and typesetting industry. Lorem Ipsum has been the industry's standard dummy text ever since the unknown printer took a galley</p>
<a class="abs btn btn-solid hero-btn">Contact Us</a>
<svg class="abs hero-arrow" style="left:30px" width="20" height="60" viewBox="0 0 20 60"><path d="M16 2L4 30l12 28" fill="none" stroke="#fff" stroke-width="2"/></svg>
<svg class="abs hero-arrow" style="left:1150px" width="20" height="60" viewBox="0 0 20 60"><path d="M4 2l12 28L4 58" fill="none" stroke="#fff" stroke-width="2"/></svg>

<section class="abs welcome"></section>
<p class="abs welcome-kicker">WELCOME TO</p>
<h2 class="abs welcome-title">BRIVANHOLDINGS</h2>
<div class="abs welcome-text">
  <p>Lorem Ipsum is simply dummy text of the printing and typesetting industry. Lorem Ipsum has been the industry's standard dummy text ever since the 1500s.</p>
  <p>Lorem Ipsum is simply dummy text of the printing and typesetting industry. Lorem Ipsum has been the industry's standard dummy text ever since the 1500s, when an unknown printer took a galley of type and scrambled it to make a type specimen book. It has survived not only five centuries, but also the leap into electronic typesetting.</p>
</div>
<a class="abs btn btn-outline welcome-btn">Learn More</a>
<div class="abs frame welcome-frame"></div>
<div class="abs welcome-photo" role="img" aria-label="Photo of tall grain silos at an industrial site"></div>

<section class="abs services"></section>
<h2 class="abs section-title" style="top:1190px">OUR BEST <b>SERVICES</b></h2>
<ul class="abs tabs">
  <li class="active" style="width:166px">Electrical</li>
  <li style="width:226px">Construction and<br>Maintenance</li>
  <li style="width:166px">Millwright</li>
  <li style="width:234px">Automation Control<br>&amp; System Integration</li>
  <li style="width:254px">Equipment Assembly<br>Repair &amp; Installation</li>
</ul>
<div class="abs frame service-frame"></div>
<div class="abs service-photo" role="img" aria-label="Photo of an electrician working at an electrical control panel"></div>
<h3 class="abs service-title">ELECTRICAL</h3>
<div class="abs service-text">
  <p>Lorem Ipsum is simply dummy text of the printing and typesetting industry. Lorem Ipsum has been the industry's standard dummy text ever since the 1500s.</p>
  <p>Lorem Ipsum is simply dummy text of the printing and typesetting industry. Lorem Ipsum has been the industry's standard dummy text ever since the 1500s, when an unknown printer took a galley of type and scrambled it to make a type specimen book. It has survived not only five centuries, but also the leap into electronic typesetting.</p>
</div>
<a class="abs btn btn-solid service-btn">Learn More</a>

<section class="abs call-band"></section>
<h2 class="abs band-title">BRIVANHOLDINGS INDUSTRIAL&amp; COMMERCIAL SERVICES</h2>
<p class="abs band-text">Lorem Ipsum is simply dummy text of the printing and typesetting industry. Lorem Ipsum has been the industry's<br>standard dummy text ever since the 1500s.</p>
<div class="abs band-call">
  <span>Call Us On</span>
  <span class="icon-circle"><svg width="34" height="34" viewBox="0 0 24 24"><path fill="#fff" d="M6.6 10.8a15.1 15.1 0 0 0 6.6 6.6l2.2-2.2c.3-.3.7-.4 1-.2 1.1.4 2.3.6 3.6.6.6 0 1 .4 1 1V20c0 .6-.4 1-1 1A17 17 0 0 1 3 4c0-.6.4-1 1-1h3.5c.6 0 1 .4 1 1 0 1.3.2 2.5.6 3.6.1.3 0 .7-.2 1z"/></svg></span>
  <span>123 456 7890</span>
</div>

<h2 class="abs section-title" style="top:2158px">LATEST <b>NEWS</b></h2>
<article class="abs news-card" style="left:78px">
  <div class="news-photo" role="img" aria-label="Photo of insulated pipework in a plant room"></div>
  <div class="news-date"><b>12</b><span>Oct</span></div>
  <h3 class="news-title">Lorem Ipsum is simply dummy text of the.</h3>
  <p class="news-text">Lorem Ipsum is simply dummy text of the printing and typesetting industry. Lorem Ipsum has been the industry's standard dummy text .</p>
</article>
<article class="abs news-card" style="left:440px">
  <div class="news-photo" role="img" aria-label="Photo of a grey electrical switchgear cabinet" style="background:linear-gradient(135deg,#a7abae,#6f767b 60%,#3c4246)"></div>
  <div class="news-date"><b>11</b><span>Oct</span></div>
  <h3 class="news-title">Lorem Ipsum is simply dummy text of the.</h3>
  <p class="news-text">Lorem Ipsum is simply dummy text of the printing and typesetting industry. Lorem Ipsum has been the industry's standard dummy text .</p>
</article>
<article class="abs news-card" style="left:802px">
  <div class="news-photo" role="img" aria-label="Photo of a worker at an industrial milling machine" style="background:linear-gradient(135deg,#b9bcbd,#6e7477 55%,#34383a)"></div>
  <div class="news-date"><b>10</b><span>Oct</span></div>
  <h3 class="news-title">Lorem Ipsum is simply dummy text of the.</h3>
  <p class="news-text">Lorem Ipsum is simply dummy text of the printing and typesetting industry. Lorem Ipsum has been the industry's standard dummy text .</p>
</article>

<div class="abs clients">
  <svg class="nav-shape" width="1046" height="106" viewBox="0 0 1046 106"><defs><linearGradient id="clg" x1="0" y1="0" x2="1" y2="0"><stop offset="0" stop-color="#0f7fc4"/><stop offset=".5" stop-color="#27aef0"/><stop offset="1" stop-color="#0f7fc4"/></linearGradient></defs><path d="M30 0H1016L1046 106H0Z" fill="url(#clg)"/></svg>
  <ul class="client-list">
    <li><i></i>FALSTO</li>
    <li>Prairie Grains</li>
    <li>Tazzik</li>
    <li><i></i>OKSU</li>
    <li><i></i>MarlowKibbleCo</li>
  </ul>
</div>

<footer class="abs site-footer"></footer>
<ul class="abs footer-nav">
  <li class="active">Home</li>
  <li>About</li>
  <li>Services</li>
  <li>Clients</li>
  <li>News</li>
  <li>Contact</li>
</ul>
<div class="abs social" aria-label="Social links">
  <span class="on"></span><span></span><span></span>
</div>
<p class="abs footer-label">CONTACT US</p>
<div class="abs contact-item" style="left:78px">
  <span class="icon-circle"><svg width="22" height="28" viewBox="0 0 24 30"><path fill="#fff" d="M12 0a10 10 0 0 0-10 10c0 8 10 20 10 20s10-12 10-20A10 10 0 0 0 12 0zm0 14a4 4 0 1 1 0-8 4 4 0 0 1 0 8z"/></svg></span>
  <span>BRIVANHOLDINGS</span>
</div>
<div class="abs contact-item" style="left:346px">
  <span class="icon-circle"><svg width="22" height="22" viewBox="0 0 24 24"><path fill="#fff" d="M6.6 10.8a15.1 15.1 0 0 0 6.6 6.6l2.2-2.2c.3-.3.7-.4 1-.2 1.1.4 2.3.6 3.6.6.6 0 1 .4 1 1V20c0 .6-.4 1-1 1A17 17 0 0 1 3 4c0-.6.4-1 1-1h3.5c.6 0 1 .4 1 1 0 1.3.2 2.5.6 3.6.1.3 0 .7-.2 1z"/></svg></span>
  <span>+ 123 456 4890</span>
</div>
<div class="abs contact-item" style="left:610px">
  <span class="icon-circle"><svg width="24" height="18" viewBox="0 0 24 18"><rect x="1" y="1" width="22" height="16" rx="2" fill="#fff"/><path d="M2 2l10 8 10-8" fill="none" stroke="#1a9fe0" stroke-width="2"/></svg></span>
  <span>info@brivanholdings.net</span>
</div>
<p class="abs copyright">©BRIVANHOLDINGS -2017 All Right<br>Reserved.</p>

</body>
</html>
```